Wedding dance company needs flyer design

I am looking for a double sided A5 flyer to be designed for my company Step Loft.

The concept of the flyer is to attract couples for their first wedding dance.

This is to support content of our website: http://www.steploftstudio.com/wedding-mix

All the text content for the flyer is attached in flyer.txt. My company logo is attached in logo.zip.

I would like to have 1-2 photos on the flyer based on a couple and their wedding first dance and perhaps some designs without photos (graphics instead).

```html
<!DOCTYPE html>
<html lang="en">
<head>
<meta charset="utf-8">
<title>Step Loft – First Dance Flyer</title>
<link href="https://fonts.googleapis.com/css2?family=Crimson+Text:wght@400;600&family=Oswald:wght@500;700&family=Amaranth&display=swap" rel="stylesheet">
<style>
:root{
  --bg:#e9e6e8;
  --magenta-deep:#7e1258;
  --magenta:#b8237a;
  --magenta-light:#d94a9c;
  --white:#ffffff;
  --ink:#3d3d3d;
  --lime:#9cc93c;
  --bronze-a:#8a5a1c;--bronze-b:#d9a652;
  --silver-a:#8d8d8d;--silver-b:#e3e3e3;
  --gold-a:#c48a00;--gold-b:#ffd34d;
  --plat-a:#9a9aa8;--plat-b:#f1f1f5;
}
*{box-sizing:border-box;margin:0;padding:0}
html,body{width:1200px;height:867px;overflow:hidden;background:var(--bg)}
.canvas{position:relative;width:1200px;height:867px}
.flyer{position:absolute;top:66px;width:520px;height:735px;overflow:hidden;box-shadow:0 6px 18px rgba(0,0,0,.25)}
.flyer-back{left:50px;background:linear-gradient(160deg,var(--magenta-deep) 0%,var(--magenta) 55%,var(--magenta-light) 100%)}
.flyer-front{left:630px;background:var(--white)}

/* back side */
.intro{position:absolute;left:34px;top:30px;width:452px;font-family:"Crimson Text",serif;font-size:12.5px;line-height:1.42;color:var(--white)}
.intro p{margin-bottom:9px}
.packages-title{position:absolute;left:34px;top:272px;font-family:"Oswald",sans-serif;font-weight:700;font-size:20px;color:var(--white);letter-spacing:.3px}
.packages{position:absolute;left:34px;top:310px;display:flex;gap:4px}
.package{width:78px;height:74px;border-radius:3px;text-align:center;font-family:"Oswald",sans-serif;font-weight:500;color:var(--magenta-deep);font-size:9.5px;line-height:1.15;padding-top:4px}
.package .tier{display:block;font-weight:700;font-size:10.5px;margin-bottom:4px}
.pkg-bronze{background:linear-gradient(180deg,var(--bronze-b),var(--bronze-a))}
.pkg-silver{background:linear-gradient(180deg,var(--silver-b),var(--silver-a))}
.pkg-gold{background:linear-gradient(180deg,var(--gold-b),var(--gold-a))}
.pkg-platinum{background:linear-gradient(180deg,var(--plat-b),var(--plat-a))}
.extras{position:absolute;left:34px;top:398px;width:300px;font-family:"Oswald",sans-serif;font-weight:500;font-size:12px;line-height:1.35;color:var(--white)}
.couple-art{position:absolute;left:250px;top:300px;width:270px;height:330px;background:radial-gradient(ellipse at 55% 45%,rgba(255,210,235,.55),rgba(255,255,255,0) 70%)}
.back-footer{position:absolute;left:0;bottom:0;width:100%;height:96px;background:var(--white);display:flex;align-items:center;padding:0 26px;gap:22px}

/* shared */
.brand{font-family:"Oswald",sans-serif;font-weight:700;color:var(--magenta);text-transform:uppercase;display:flex;align-items:center;gap:6px}
.brand-mark{display:inline-block;background:var(--lime)}
.back-footer .brand{font-size:22px}
.back-footer .brand-mark{width:9px;height:9px}
.contact-cols{display:flex;gap:22px}
.contact-list{list-style:none;font-family:"Oswald",sans-serif;font-weight:500;font-size:9.5px;color:var(--ink)}
.contact-list li{display:flex;align-items:center;gap:6px;height:15px;white-space:nowrap}
.icon{width:11px;height:11px;flex:none}

/* front side */
.photo-grid{position:absolute;left:0;top:0;width:520px;height:480px;display:grid;grid-template-columns:repeat(3,1fr);grid-template-rows:repeat(3,1fr);gap:3px;padding:3px;background:var(--white)}
.photo{width:100%;height:100%}
.ph-beach{background:linear-gradient(180deg,#7fc1ea,#cfe6ef 55%,#e8dcc4)}
.ph-lawn{background:linear-gradient(180deg,#cfd9e3,#f3f3f3 60%,#8fae7a)}
.ph-indoor{background:linear-gradient(180deg,#efe8df,#d8cfc6)}
.ph-pavement{background:linear-gradient(160deg,#a9a9a6,#cfc9c0 60%,#e4c1cc)}
.ph-rocks{background:linear-gradient(180deg,#5fb3e5,#9ed3ef 45%,#5a4638)}
.ph-sea{background:linear-gradient(180deg,#9fd3ef,#5fbad0 60%,#e9e2d6)}
.ph-garden{background:linear-gradient(180deg,#a5cf6b,#3f7d2f)}
.ph-palm{background:linear-gradient(180deg,#2a8fd9,#7ec6ec 55%,#f4efe4)}
.tagline-cell{background:linear-gradient(160deg,var(--magenta-deep),var(--magenta));display:flex;flex-direction:column;justify-content:center;align-items:center;text-align:center;color:var(--white);font-family:"Amaranth",sans-serif}
.tagline-main{font-size:25px;line-height:1.1}
.tagline-sub{font-size:15px;line-height:1.15;margin-top:6px}
.front-footer{position:absolute;left:0;top:480px;width:100%;height:255px}
.front-footer .brand{position:absolute;left:0;width:100%;justify-content:center;top:26px;font-size:40px}
.front-footer .brand-mark{width:14px;height:14px}
.front-footer .contact-list{position:absolute;left:24px;top:96px;font-size:13px}
.front-footer .contact-list li{height:22px;gap:9px}
.front-footer .icon{width:15px;height:15px}
.swirl-art{position:absolute;right:0;bottom:0;width:200px;height:150px;background:radial-gradient(ellipse at 80% 75%,rgba(217,74,156,.35),rgba(255,255,255,0) 70%)}
</style>
</head>
<body>
<main class="canvas">

  <section class="flyer flyer-back" aria-label="Flyer back">
    <div class="intro">
      <p>Are you feeling nervous about your first dance? Then why not let Step Loft take care of all the planning for you!</p>
      <p>Step Loft specialise in preparing couples for their first dance to ensure it's memorable.</p>
      <p>Lessons can take place in a studio of your choice or in the comfort of your own home. We provide a wide range of dance styles and various packages to suit all budgets. Step Loft, a small family business, provide flexibility and personal touches to make you feel comfortable and confident on the dance floor. Whether you want simple steps, a classic Waltz or a glitzy extravaganza, you'll soon be able to wow your friends and family.</p>
      <p>Your bespoke first wedding dance will match your song, natural style and ability, so it will never be too difficult and will suit you perfectly.</p>
    </div>

    <div class="couple-art" role="img" aria-label="Swirling silhouette of a dancing bride and groom"></div>

    <h2 class="packages-title">PACKAGES (STARTING AT £65)</h2>
    <div class="packages">
      <div class="package pkg-bronze"><span class="tier">Bronze</span>Package<br>1 x 1<br>hour lesson</div>
      <div class="package pkg-silver"><span class="tier">Silver</span>Package<br>1 x 90<br>minute lesson</div>
      <div class="package pkg-gold"><span class="tier">Gold</span>Package<br>2 x 90<br>minute lessons</div>
      <div class="package pkg-platinum"><span class="tier">Platinum</span>Package<br>1 x 2 hour lesson<br>&amp; 2 x 90<br>minute lessons</div>
    </div>
    <p class="extras">We also offer the SOS last minute package, on-site rehearsals, hen parties and gift vouchers.</p>

    <footer class="back-footer">
      <div class="brand"><span class="brand-mark"></span>Step Loft</div>
      <div class="contact-cols">
        <ul class="contact-list">
          <li><svg class="icon" viewBox="0 0 12 12"><rect width="12" height="12" rx="2" fill="#b8237a"/><path d="M3.5 2.5h1.5l.8 2-1 .8a5 5 0 0 0 2 2l.8-1 2 .8v1.5c0 .6-.5 1-1 1A6.5 6.5 0 0 1 2.5 3.5c0-.5.4-1 1-1z" fill="#fff"/></svg>07700900418 / 07700900419</li>
          <li><svg class="icon" viewBox="0 0 12 12"><rect width="12" height="12" rx="2" fill="#9cc93c"/><rect x="2.5" y="3.5" width="7" height="5" fill="none" stroke="#fff"/><path d="M2.5 3.5 6 6.5l3.5-3" fill="none" stroke="#fff"/></svg>info@steploftstudio.com</li>
          <li><svg class="icon" viewBox="0 0 12 12"><rect width="12" height="12" rx="2" fill="#7e1258"/><circle cx="6" cy="6" r="3.5" fill="none" stroke="#fff"/><path d="M2.5 6h7M6 2.5v7" stroke="#fff" stroke-width=".8"/></svg>www.steploftstudio.com</li>
        </ul>
        <ul class="contact-list">
          <li><svg class="icon" viewBox="0 0 12 12"><rect width="12" height="12" rx="2" fill="#6aa7d8"/></svg>Social - @StepLoftCo</li>
          <li><svg class="icon" viewBox="0 0 12 12"><rect width="12" height="12" rx="2" fill="#4a6aa8"/></svg>stepbook.net/steploftstudio</li>
          <li><svg class="icon" viewBox="0 0 12 12"><rect width="12" height="12" rx="2" fill="#c4302b"/></svg>www.steplofttv.com</li>
        </ul>
      </div>
    </footer>
  </section>

  <section class="flyer flyer-front" aria-label="Flyer front">
    <div class="photo-grid">
      <div class="photo ph-beach" role="img" aria-label="Wedding couple's feet resting on a boat by the sea"></div>
      <div class="photo ph-lawn" role="img" aria-label="Bride and groom dancing outdoors"></div>
      <div class="photo ph-indoor" role="img" aria-label="Groom holding the bride in a first dance"></div>
      <div class="photo ph-pavement" role="img" aria-label="Couple dancing seen from above with a bouquet"></div>
      <div class="tagline-cell">
        <p class="tagline-main">Make your<br>First Dance</p>
        <p class="tagline-sub">a performance<br>to be remembered.</p>
      </div>
      <div class="photo ph-rocks" role="img" aria-label="Bride and groom embracing on rocks by the sea"></div>
      <div class="photo ph-sea" role="img" aria-label="Groom lifting the bride by the water"></div>
      <div class="photo ph-garden" role="img" aria-label="Couple dancing on a green lawn"></div>
      <div class="photo ph-palm" role="img" aria-label="Bride on a palm tree over a tropical beach"></div>
    </div>

    <footer class="front-footer">
      <div class="brand"><span class="brand-mark"></span>Step Loft</div>
      <ul class="contact-list">
        <li><svg class="icon" viewBox="0 0 12 12"><rect width="12" height="12" rx="2" fill="#b8237a"/><path d="M3.5 2.5h1.5l.8 2-1 .8a5 5 0 0 0 2 2l.8-1 2 .8v1.5c0 .6-.5 1-1 1A6.5 6.5 0 0 1 2.5 3.5c0-.5.4-1 1-1z" fill="#fff"/></svg>07700900418 / 07700900419</li>
        <li><svg class="icon" viewBox="0 0 12 12"><rect width="12" height="12" rx="2" fill="#9cc93c"/><rect x="2.5" y="3.5" width="7" height="5" fill="none" stroke="#fff"/><path d="M2.5 3.5 6 6.5l3.5-3" fill="none" stroke="#fff"/></svg>info@steploftstudio.com</li>
        <li><svg class="icon" viewBox="0 0 12 12"><rect width="12" height="12" rx="2" fill="#7e1258"/><circle cx="6" cy="6" r="3.5" fill="none" stroke="#fff"/><path d="M2.5 6h7M6 2.5v7" stroke="#fff" stroke-width=".8"/></svg>www.steploftstudio.com</li>
      </ul>
      <div class="swirl-art" role="img" aria-label="Pink swirl ornament"></div>
    </footer>
  </section>

</main>
</body>
</html>
```